Corporate Power Point Template

Tarnel Holdings, Inc. produces and sells ready-mixed concrete, aggregates, and concrete-related products and services for the construction industry in the United States.

We are looking for a simple and sleek design that will look great on a projector, as well as when printed on paper. We prefer a lighter background color that will not waste ink when printed. We would also like to stay away from wavy banners, or over-the-top graphics that take away from usable space in the deck. Please use a variation of the color scheme in the "Brand Standards" file attached.

Construction

```html
<!DOCTYPE html>
<html lang="en">
<head>
<meta charset="utf-8">
<title>Tarnel Holdings – Corporate Template</title>
<link href="https://fonts.googleapis.com/css2?family=Carlito:wght@400;700&display=swap" rel="stylesheet">
<style>
:root{
  --red:#c8202f;
  --red-soft:rgba(200,32,47,.85);
  --ink:#4a4a4a;
  --grey:#6d6d6d;
  --grey-box:#6b6b6b;
  --rule:#9a9a9a;
  --frame:#a8a8a8;
  --paper:#ffffff;
  --photo-a:#d9d9d9;
  --photo-b:#8a8a8a;
  --photo-c:#4f4f4f;
}
*{box-sizing:border-box;margin:0;padding:0}
html,body{width:1200px;height:763px;overflow:hidden;background:#fff}
body{position:relative;font-family:"Carlito","Calibri",sans-serif;color:var(--ink)}
.slide{position:absolute;width:396px;height:248px;border:1px solid var(--frame);background:var(--paper);overflow:hidden}
.c1{left:2px}.c2{left:405px}.c3{left:808px}
.r1{top:2px}.r2{top:257px}.r3{top:517px}
.photo{position:absolute;background:linear-gradient(170deg,var(--photo-a) 0%,var(--photo-b) 45%,var(--photo-c) 100%)}
.photo.full{inset:0}
/* brand name */
.brand{position:absolute;display:flex;align-items:center;gap:4px;color:var(--grey);font-weight:700;line-height:.95;text-transform:uppercase}
.brand .mark{background:var(--red);flex:none}
.brand.large{font-size:19px}
.brand.large .mark{width:12px;height:12px}
.brand.small{right:6px;top:5px;font-size:8px}
.brand.small .mark{width:6px;height:6px}
.brand.light{color:#fff}
/* titles */
.title{position:absolute;left:26px;top:6px;color:var(--red);font-weight:700;font-size:14px}
.title.grey{color:var(--grey)}
.underline{position:absolute;left:26px;top:26px;display:flex;gap:4px}
.underline span{width:24px;height:2px;background:#c4c4c4}
.underline span:first-child{background:var(--red)}
.underline span:nth-child(2){background:#777}
.underline span:nth-child(3){background:#999}
.bullets{position:absolute;list-style:none;font-size:7px;line-height:1.3;color:var(--grey)}
.bullets li{position:relative;padding-left:12px;margin-bottom:7px}
.bullets li::before{content:"";position:absolute;left:2px;top:3px;width:2px;height:2px;background:var(--red)}
/* footer */
.footer{position:absolute;left:0;right:0;bottom:0;height:19px;border-top:1px solid var(--red);background:linear-gradient(90deg,#e6e6e6,#c9c9c9 40%,#e0e0e0 70%,#d2d2d2)}
.page{position:absolute;left:7px;top:4px;width:10px;height:10px;border-radius:50%;background:var(--red);color:#fff;font-size:6px;text-align:center;line-height:10px}
.page.outline{background:none;border:1px solid #fff}
.copy{position:absolute;left:0;right:0;text-align:center;font-size:6px;color:var(--red)}
.footer .copy{top:5px}
.badges{position:absolute;right:6px;top:3px;display:flex;gap:3px;align-items:center}
.badges i{display:block;height:11px;background:#fff;border:1px solid #777}
.badges i.r{border-radius:50%;width:11px}
.badges i.w{width:22px}.badges i.s{width:11px}
/* slide 1 */
.s1 .photo{top:55px;left:0;right:0;height:133px}
.s1 .band{position:absolute;left:35px;right:35px;top:92px;height:40px;background:rgba(90,90,90,.45)}
.s1 h1{position:absolute;left:0;right:0;top:102px;text-align:center;color:#fff;font-size:22px;font-weight:700}
.s1 .redband{position:absolute;left:0;right:0;top:188px;bottom:0;background:var(--red)}
.s1 .sub{position:absolute;left:0;right:0;top:12px;text-align:center;color:#fff;font-size:12px}
.s1 .redband .copy{top:46px;color:#fff;font-weight:700}
/* slide 2 */
.s2 .photo{inset:0}
.s2 .veil{position:absolute;left:0;top:0;bottom:0;width:196px;background:rgba(255,255,255,.82)}
.s2 h1{position:absolute;left:8px;top:135px;color:var(--red);font-size:20px;font-weight:700;line-height:1.25}
.s2 .v2{position:absolute;left:8px;top:202px;font-size:11px;color:#888}
.s2 .copy{left:60px;right:auto;top:235px;color:#999}
/* section slides */
.wedge{position:absolute;inset:0;clip-path:polygon(0 0,100% 100%,0 100%)}
.wedge.grey{background:rgba(110,110,110,.75);clip-path:polygon(0 0,30% 0,100% 100%,0 100%)}
.wedge.red{background:var(--red-soft)}
.section h2{position:absolute;left:14px;top:178px;color:#fff;font-size:16px;font-weight:700}
.section .page{top:230px}
.section .copy{top:232px;color:#fff}
/* process boxes */
.pbox{position:absolute;top:73px;width:86px;height:103px;background:var(--grey-box);border-radius:3px;color:#fff;font-size:6.5px;font-weight:700;line-height:1.3;text-align:center;padding:10px 6px}
.arrow{position:absolute;top:154px;width:0;height:0;border-top:6px solid transparent;border-bottom:6px solid transparent;border-left:9px solid var(--red)}
/* cycle */
.cycle{position:absolute;left:0;top:0}
.cbox{position:absolute;width:57px;height:37px;background:var(--red);border-radius:4px;color:#fff;font-size:7px;font-weight:700;text-align:center;line-height:1.25;display:flex;align-items:center;justify-content:center}
/* closing */
.s9 h2{position:absolute;left:0;right:0;top:105px;text-align:center;color:#fff;font-size:20px;font-weight:700}
.s9 .brand.small{left:205px;right:auto;top:10px}
.s9 .copy{top:232px;color:#fff}
.s9 .page{top:230px}
</style>
</head>
<body>

<!-- 1 : cover -->
<section class="slide c1 r1 s1">
  <div class="brand large" style="left:8px;top:10px"><span class="mark"></span><span>Tarnel<br>Holdings</span></div>
  <div class="photo" role="img" aria-label="Black and white aerial view of a city skyline"></div>
  <div class="band"></div>
  <h1>Company Presentation</h1>
  <div class="redband">
    <p class="sub">Lorem ipsum dolor sit amet</p>
    <p class="copy">© Tarnel Holdings 2017</p>
  </div>
</section>

<!-- 2 : cover v2 -->
<section class="slide c2 r1 s2">
  <div class="photo" role="img" aria-label="Black and white aerial view of a city skyline"></div>
  <div class="veil"></div>
  <div class="brand large" style="left:5px;top:8px"><span class="mark"></span><span>Tarnel<br>Holdings</span></div>
  <h1>Company<br>Presentation</h1>
  <p class="v2">Cover Slide v2</p>
  <p class="copy">© Tarnel Holdings 2017</p>
</section>

<!-- 3 : bullets -->
<section class="slide c3 r1">
  <h2 class="title">Lorem ipsum dolor sit amet</h2>
  <div class="underline"><span></span><span></span><span></span><span></span><span></span></div>
  <div class="brand small"><span class="mark"></span><span>Tarnel<br>Holdings</span></div>
  <ul class="bullets" style="left:28px;top:34px;width:340px">
    <li>Sed ut perspiciatis unde omnis iste natus error sit voluptatem accusantium doloremque laudantium, totam rem aperiam, eaque ipsa quae ab illo inventore veritatis et quasi architecto beatae vitae dicta sunt explicabo.</li>
    <li>Nemo enim ipsam voluptatem quia voluptas sit aspernatur aut odit aut fugit, sed quia consequuntur magni dolores eos qui ratione voluptatem sequi nesciunt.</li>
    <li>Neque porro quisquam est, qui dolorem ipsum quia dolor sit amet, consectetur, adipisci velit, sed quia non numquam eius modi tempora incidunt ut labore et dolore magnam aliquam quaerat voluptatem.</li>
    <li>Ut enim ad minima veniam, quis nostrum exercitationem ullam corporis suscipit laboriosam, nisi ut aliquid ex ea commodi consequatur?</li>
    <li>Quis autem vel eum iure reprehenderit qui in ea voluptate velit esse quam nihil molestiae consequatur, vel illum qui dolorem eum fugiat quo voluptas nulla pariatur?</li>
  </ul>
  <footer class="footer"><span class="page">2</span><p class="copy">© Tarnel Holdings 2017</p>
    <div class="badges"><i class="s"></i><i class="r"></i><i class="w"></i><i class="w"></i><i class="r"></i></div></footer>
</section>

<!-- 4 : section grey -->
<section class="slide c1 r2 section">
  <div class="photo full" role="img" aria-label="Black and white aerial view of a city skyline"></div>
  <div class="wedge grey"></div>
  <div class="brand small light"><span class="mark"></span><span>Tarnel<br>Holdings</span></div>
  <h2>Section Slide</h2>
  <span class="page outline">1</span>
  <p class="copy">© Tarnel Holdings 2017</p>
</section>

<!-- 5 : two columns -->
<section class="slide c2 r2">
  <h2 class="title grey">Lorem ipsum dolor sit amet</h2>
  <div class="underline"><span></span><span></span><span></span><span></span><span></span></div>
  <div class="brand small"><span class="mark"></span><span>Tarnel<br>Holdings</span></div>
  <ul class="bullets" style="left:26px;top:34px;width:168px">
    <li>Sed ut perspiciatis unde omnis iste natus error sit voluptatem accusantium doloremque laudantium, totam rem aperiam, eaque ipsa quae ab illo inventore veritatis et quasi architecto beatae vitae dicta sunt explicabo.</li>
    <li>Nemo enim ipsam voluptatem quia voluptas sit aspernatur aut odit aut fugit, sed quia consequuntur magni dolores eos qui ratione voluptatem sequi nesciunt.</li>
    <li>Neque porro quisquam est, qui dolorem ipsum quia dolor sit amet, consectetur, adipisci velit, sed quia non numquam eius modi tempora incidunt ut labore et dolore magnam aliquam quaerat voluptatem.</li>
  </ul>
  <ul class="bullets" style="left:206px;top:34px;width:168px">
    <li>Sed ut perspiciatis unde omnis iste natus error sit voluptatem accusantium doloremque laudantium, totam rem aperiam, eaque ipsa quae ab illo inventore veritatis et quasi architecto beatae vitae dicta sunt explicabo.</li>
    <li>Nemo enim ipsam voluptatem quia voluptas sit aspernatur aut odit aut fugit, sed quia consequuntur magni dolores eos qui ratione voluptatem sequi nesciunt.</li>
    <li>Neque porro quisquam est, qui dolorem ipsum quia dolor sit amet, consectetur, adipisci velit, sed quia non numquam eius modi tempora incidunt ut labore et dolore magnam aliquam quaerat voluptatem.</li>
  </ul>
  <footer class="footer"><span class="page">3</span><p class="copy">© Tarnel Holdings 2017</p>
    <div class="badges"><i class="s"></i><i class="r"></i><i class="w"></i><i class="w"></i><i class="r"></i></div></footer>
</section>

<!-- 6 : section red -->
<section class="slide c3 r2 section">
  <div class="photo full" role="img" aria-label="Black and white aerial view of a city skyline"></div>
  <div class="wedge red"></div>
  <div class="brand small light"><span class="mark" style="background:#fff"></span><span>Tarnel<br>Holdings</span></div>
  <h2>Section Slide</h2>
  <span class="page outline">4</span>
  <p class="copy">© Tarnel Holdings 2017</p>
</section>

<!-- 7 : process -->
<section class="slide c1 r3">
  <h2 class="title">Lorem ipsum dolor sit amet</h2>
  <div class="underline"><span></span><span></span><span></span><span></span><span></span></div>
  <div class="brand small"><span class="mark"></span><span>Tarnel<br>Holdings</span></div>
  <div class="pbox" style="left:63px">Sed ut perspiciatis unde omnis iste natus error sit voluptatem accusantium doloremque laudantium, totam rem aperiam, eaque ipsa quae ab illo inventore veritatis et quasi.</div>
  <span class="arrow" style="left:147px"></span>
  <div class="pbox" style="left:155px">Sed ut perspiciatis unde omnis iste natus error sit voluptatem accusantium doloremque laudantium, totam rem aperiam, eaque ipsa quae ab illo inventore veritatis et quasi.</div>
  <span class="arrow" style="left:239px"></span>
  <div class="pbox" style="left:247px">Sed ut perspiciatis unde omnis iste natus error sit voluptatem accusantium doloremque laudantium, totam rem aperiam, eaque ipsa quae ab illo inventore veritatis et quasi.</div>
  <footer class="footer"><span class="page">6</span><p class="copy">© Tarnel Holdings 2017</p>
    <div class="badges"><i class="s"></i><i class="r"></i><i class="w"></i><i class="w"></i><i class="r"></i></div></footer>
</section>

<!-- 8 : cycle -->
<section class="slide c2 r3">
  <h2 class="title">Lorem ipsum dolor sit amet</h2>
  <div class="underline"><span></span><span></span><span></span><span></span><span></span></div>
  <div class="brand small"><span class="mark"></span><span>Tarnel<br>Holdings</span></div>
  <svg class="cycle" width="396" height="248" aria-hidden="true"><circle cx="198" cy="130" r="76" fill="none" stroke="#b5b5b5" stroke-width="1"/></svg>
  <div class="cbox" style="left:170px;top:36px">Sed ut<br>perspiciatis</div>
  <div class="cbox" style="left:240px;top:88px">Sed ut<br>perspiciatis</div>
  <div class="cbox" style="left:213px;top:171px">Sed ut<br>perspiciatis</div>
  <div class="cbox" style="left:125px;top:171px">Sed ut<br>perspiciatis</div>
  <div class="cbox" style="left:98px;top:88px">Sed ut<br>perspiciatis</div>
  <footer class="footer"><span class="page">7</span><p class="copy">© Tarnel Holdings 2017</p>
    <div class="badges"><i class="s"></i><i class="r"></i><i class="w"></i><i class="w"></i><i class="r"></i></div></footer>
</section>

<!-- 9 : closing -->
<section class="slide c3 r3 s9">
  <div class="photo full" role="img" aria-label="Black and white aerial view of a city skyline"></div>
  <div class="brand small light"><span class="mark"></span><span>Tarnel</span></div>
  <h2>Thank You For Your Time</h2>
  <span class="page outline">8</span>
  <p class="copy">© Tarnel Holdings 2017</p>
</section>

</body>
</html>
```